Fernvale Craft Works business card design- Fine Art sculpture business (Contract guaranteed)

This business card is for a fine art business. Though we don't have a website up and running yet it should be up soon. I would like the business card to be elegant and fairly simple with a picture of one of my sculptures on the front (you might need to photoshop out the background) as well as my basic contact info (my name,phone # and e-mail). On the back I'd like it to be pretty simple with just "Notes" and some blank lines for writing in info.

Target Market(s)

High end artwork buyers

Industry/Entity Type

Art Gallery

Contact Information for Business Card

Marlo Prewitt Phone: (555) 213-4098 E-mail: marlo@quillbrookmail.com plain square marker: @fernvalecraftworks plain square marker: fernvalecraftworks

Colors

Designer to choose colors to be used in the design.

Requirements
Must have
• *A picture of one of my sculptures*, my name, business name (Fernvale Craft Works), e-mail, phone #, and a notes section on the back.
• Fernvale Craft Works
• Marlo Prewitt
• (555)213-4098
• marlo@quillbrookmail.com
• plain square marker: @fernvalecraftworks
• plain square marker: fernvalecraftworks
Nice to have
• It'd be nice if you can crop out the background in the sculpture pictures, which ever one you end up using.

```html
<!DOCTYPE html>
<html lang="en">
<head>
<meta charset="utf-8">
<title>Fernvale Craft Works – Business Card</title>
<link href="https://fonts.googleapis.com/css2?family=Source+Sans+3:ital,wght@0,400;0,600;1,400&display=swap" rel="stylesheet">
<style>
  :root {
    --backdrop: #9c9c9c;
    --card-white: #ffffff;
    --panel-dark: #262626;
    --ink: #1a1a1a;
    --ink-soft: #333333;
    --rule: #8a8a8a;
    --icon: #555555;
    --stone-deep: #0e2a1f;
    --stone-mid: #1f6b4a;
    --stone-light: #4fa982;
    --social-mark: #4a4a4a;
  }
  * { box-sizing: border-box; margin: 0; padding: 0; }
  html, body {
    width: 1050px;
    height: 1200px;
    overflow: hidden;
  }
  body {
    background: var(--backdrop);
    font-family: "Source Sans 3", "Helvetica Neue", Arial, sans-serif;
    color: var(--ink);
    position: relative;
  }

  /* Front of card */
  .card-front {
    position: absolute;
    left: 228px;
    top: 172px;
    width: 620px;
    height: 354px;
    background: var(--card-white);
    display: flex;
  }
  .sculpture-panel {
    width: 264px;
    height: 100%;
    background: var(--panel-dark);
    position: relative;
  }
  .sculpture-photo {
    position: absolute;
    left: 76px;
    top: 34px;
    width: 96px;
    height: 282px;
    border-radius: 30px 36px 18px 18px;
    background: linear-gradient(160deg, var(--stone-light) 0%, var(--stone-mid) 40%, var(--stone-deep) 100%);
  }
  .contact-side {
    flex: 1;
    position: relative;
  }
  .name-block {
    position: absolute;
    left: 179px;
    top: 38px;
    height: 70px;
    border-left: 1.5px solid var(--rule);
    padding-left: 11px;
    display: flex;
    align-items: center;
  }
  .person-name {
    font-size: 18px;
    font-weight: 600;
    letter-spacing: 0.1px;
    color: var(--ink);
  }
  .contact-line {
    position: absolute;
    right: 32px;
    display: flex;
    align-items: center;
    gap: 9px;
    font-size: 16px;
    color: var(--ink-soft);
  }
  .contact-phone { top: 167px; }
  .contact-email { top: 206px; }
  .contact-icon { width: 17px; height: 17px; flex: none; }

  .social-row {
    position: absolute;
    right: 34px;
    top: 288px;
    display: flex;
    align-items: center;
    font-size: 14.5px;
    color: var(--ink-soft);
  }
  .social-handle { display: flex; align-items: center; gap: 5px; }
  .social-marker {
    width: 12px;
    height: 12px;
    background: var(--social-mark);
    flex: none;
  }
  .social-divider {
    width: 1.5px;
    height: 20px;
    background: var(--rule);
    margin: 0 11px;
  }

  /* Back of card */
  .card-back {
    position: absolute;
    left: 289px;
    top: 776px;
    width: 497px;
    height: 283px;
    background: var(--card-white);
  }
  .notes-title {
    position: absolute;
    top: 92px;
    width: 100%;
    text-align: center;
    font-style: italic;
    font-size: 13px;
    color: var(--ink);
  }
  .notes-line {
    position: absolute;
    left: 58px;
    width: 379px;
    height: 1px;
    background: var(--rule);
  }
  .notes-line--1 { top: 142px; }
  .notes-line--2 { top: 171px; }
  .notes-line--3 { top: 199px; }
</style>
</head>
<body>

  <section class="card-front" aria-label="Business card front">
    <div class="sculpture-panel">
      <div class="sculpture-photo" role="img" aria-label="Photograph of a polished green malachite stone sculpture on a round dark base"></div>
    </div>
    <div class="contact-side">
      <div class="name-block">
        <span class="person-name">Marlo Prewitt</span>
      </div>

      <div class="contact-line contact-phone">
        <span>(555) 213-4098</span>
        <svg class="contact-icon" viewBox="0 0 20 20" aria-hidden="true">
          <circle cx="10" cy="10" r="9" fill="none" stroke="var(--icon)" stroke-width="1.2"/>
          <path d="M7 5.5 L8.6 5.5 L9.3 8 L8.2 8.9 C8.8 10.3 9.7 11.2 11.1 11.8 L12 10.7 L14.5 11.4 L14.5 13 C14.5 13.6 14 14 13.4 14 C9.4 13.6 6.4 10.6 6 6.6 C6 6 6.4 5.5 7 5.5 Z" fill="none" stroke="var(--icon)" stroke-width="1.1" stroke-linejoin="round"/>
        </svg>
      </div>

      <div class="contact-line contact-email">
        <span>marlo@quillbrookmail.com</span>
        <svg class="contact-icon" viewBox="0 0 20 20" aria-hidden="true">
          <circle cx="10" cy="10" r="9" fill="none" stroke="var(--icon)" stroke-width="1.2"/>
          <rect x="5.5" y="7" width="9" height="6.5" fill="none" stroke="var(--icon)" stroke-width="1.1"/>
          <path d="M5.5 7 L10 10.8 L14.5 7" fill="none" stroke="var(--icon)" stroke-width="1.1"/>
        </svg>
      </div>

      <div class="social-row">
        <span class="social-handle"><span class="social-marker"></span>@ fernvalecraftworks</span>
        <span class="social-divider"></span>
        <span class="social-handle"><span class="social-marker"></span># fernvalecraftworks</span>
      </div>
    </div>
  </section>

  <section class="card-back" aria-label="Business card back">
    <p class="notes-title">Notes</p>
    <div class="notes-line notes-line--1"></div>
    <div class="notes-line notes-line--2"></div>
    <div class="notes-line notes-line--3"></div>
  </section>

</body>
</html>
```